Professional Letterhead for electronic use

I would like to inquire, if you could help me to create a letterhead, mostly for electronic use. Preferably in word file, with fixed letterhead design (header and footer), but will allow to add text on the main body of the letter. I usually operate online and would like to be able to add text, convert it to PDF and send as an attachment.
Target Market(s)
High net worth clients.
Industry/Entity Type
Real Estate Agent
Font styles to use
Other font styles liked:
- Century Gothic
Requirements
Must have
- Company name, logo, full address, email address, landline number, website address, Brackwell Panel logo, TOVE logo, Company registration number
Nice to have
- Professional and elegant design

```html
<!DOCTYPE html>
<html lang="en">
<head>
<meta charset="utf-8">
<title>Varenne Estate Agents – Letterhead</title>
<link rel="stylesheet" href="https://fonts.googleapis.com/css2?family=Questrial&display=swap">
<style>
  :root {
    --backdrop: #e8ebed;
    --paper: #ffffff;
    --plum: #4e1a37;
    --plum-deep: #431630;
    --orange: #ef5a1f;
    --orange-light: #f48a55;
    --orange-red: #e63a16;
    --ink: #3a3a3a;
    --rule: #6b2446;
  }
  * { box-sizing: border-box; margin: 0; padding: 0; }
  html, body { width: 1200px; height: 784px; overflow: hidden; }
  body {
    background: var(--backdrop);
    font-family: "Questrial", "Century Gothic", sans-serif;
    position: relative;
  }
  .sheet {
    position: absolute;
    top: 45px;
    width: 513px;
    height: 696px;
    border-radius: 12px;
    overflow: hidden;
    box-shadow: 0 2px 6px rgba(0,0,0,0.18);
  }
  .letter-front { left: 42px; background: var(--paper); }
  .letter-back {
    left: 634px;
    background: linear-gradient(160deg, #561c3c 0%, var(--plum) 45%, var(--plum-deep) 100%);
  }
  .sheet-waves { position: absolute; inset: 0; }

  .brand-header {
    position: absolute;
    top: 30px; left: 0; width: 100%;
    display: flex; justify-content: center; align-items: center; gap: 18px;
  }
  .brand-dot {
    width: 62px; height: 62px; border-radius: 50%;
    background: var(--orange);
  }
  .brand-words { display: flex; flex-direction: column; }
  .brand-name {
    color: var(--plum);
    font-size: 25px; letter-spacing: 5px; line-height: 1;
  }
  .brand-tagline {
    color: var(--orange);
    font-size: 10.5px; letter-spacing: 2.6px; margin-top: 8px;
  }
  .web-rule {
    position: absolute;
    top: 100px; left: 92px; width: 318px;
    display: flex; align-items: center; gap: 8px;
    color: var(--plum); font-size: 10px; letter-spacing: 1.6px; font-weight: bold;
  }
  .web-rule::before, .web-rule::after {
    content: ""; flex: 1; height: 1px; background: var(--rule);
  }

  .letter-body {
    position: absolute;
    top: 136px; left: 40px; width: 424px;
    color: var(--ink);
    font-size: 10.4px; line-height: 18.3px;
    text-align: justify; hyphens: auto;
  }
  .letter-body p + p { margin-top: 18px; }

  .signature {
    position: absolute;
    top: 577px; left: 375px;
    color: var(--ink);
  }
  .signature-name { font-size: 14px; }
  .signature-role { font-size: 9px; margin-top: 8px; }

  .memberships {
    position: absolute;
    top: 586px; left: 34px;
    display: flex; align-items: center; gap: 28px;
  }
  .badge-panel { width: 70px; height: 24px; background: #1d3e7a; }
  .badge-tove { width: 40px; height: 34px; border-radius: 50%; background: #2e8b3a; }

  .contact-strip {
    position: absolute;
    bottom: 10px; left: 0; width: 100%;
    display: flex; justify-content: center; gap: 16px;
    color: #ffffff; font-size: 9px;
  }
  .contact-item { display: flex; align-items: center; gap: 5px; }
  .contact-item svg { width: 9px; height: 9px; fill: #ffffff; }

  .binder-tab {
    position: absolute;
    right: 0; top: 155px;
    width: 36px; height: 215px;
    border-radius: 18px 0 0 18px;
    background: rgba(0,0,0,0.08);
  }
  .cover-mark {
    position: absolute;
    top: 375px; left: 50%; transform: translateX(-50%);
    width: 130px; height: 130px; border-radius: 50%;
    background: linear-gradient(135deg, var(--orange-light), var(--orange-red));
  }
  .cover-name {
    position: absolute;
    top: 548px; left: 0; width: 100%;
    text-align: center;
    color: #ffffff; font-size: 36px; letter-spacing: 8px;
  }
  .cover-tagline {
    position: absolute;
    top: 603px; left: 0; width: 100%;
    text-align: center;
    color: var(--orange); font-size: 14px; letter-spacing: 4.5px;
  }
</style>
</head>
<body>

<section class="sheet letter-front" aria-label="Letterhead page">
  <svg class="sheet-waves" viewBox="0 0 513 696" preserveAspectRatio="none" aria-hidden="true">
    <defs>
      <linearGradient id="waveTop" x1="0" y1="0" x2="1" y2="0.4">
        <stop offset="0" stop-color="#e63a16"/>
        <stop offset="0.6" stop-color="#f06a2e"/>
        <stop offset="1" stop-color="#f4955e"/>
      </linearGradient>
      <linearGradient id="waveBottom" x1="0" y1="1" x2="1" y2="0">
        <stop offset="0" stop-color="#e63a16"/>
        <stop offset="0.5" stop-color="#f07a40"/>
        <stop offset="1" stop-color="#f4955e"/>
      </linearGradient>
    </defs>
    <rect width="513" height="350" fill="url(#waveTop)"/>
    <rect y="350" width="513" height="346" fill="url(#waveBottom)"/>
    <path fill="#ffffff"
      d="M0,245 C6,190 22,120 70,72 C118,28 200,16 285,13 C370,10 440,2 513,14
         V545 C492,600 445,628 385,640 C305,655 250,628 155,632 C85,636 32,650 0,668 Z"/>
  </svg>

  <header class="brand-header">
    <span class="brand-dot" aria-hidden="true"></span>
    <div class="brand-words">
      <span class="brand-name">VARENNE</span>
      <span class="brand-tagline">ESTATE AGENTS</span>
    </div>
  </header>
  <div class="web-rule">www.varenneestate.org</div>

  <main class="letter-body">
    <p>Lorem ipsum dolor sit amet, consectetur adipiscing elit. Donec orci purus, luctus vitae dignissim eu, iaculis sed purus. Vivamus faucibus, ipsum nec aliquet viverra, leo mauris condimentum ligula, sit amet sagittis enim ligula quis arcu. Nam egestas tortor id nisi porttitor mattis. In tortor ante, ultricies in suscipit a, tempus non massa. Vivamus et auctor mi. Fusce vel massa nulla. Phasellus nec eros mauris, et scelerisque orci. Donec malesuada orci vitae nulla accumsan porta a id massa.</p>
    <p>Quisque accumsan iaculis magna sit amet fringilla. Maecenas consequat, magna eget tincidunt semper, odio nibh rutrum mi, id feugiat ante nisi eu risus. Vestibulum nunc orci, rhoncus a placerat in, ultricies in mi. Cras mattis varius eros, vel fringilla nisi suscipit eget. Quisque scelerisque sagittis nulla at porttitor. Mauris a justo et tellus interdum tristique. Sed id augue vitae urna euismod commodo aliquet a quam. Pellentesque arcu velit, cursus et malesuada ut, consequat et diam. Nullam erat sem, rhoncus id ullamcorper vitae, rhoncus et arcu. In ultricies ultricies nulla.</p>
    <p>Kut rutrum nisi iaculis at. Donec eu magna a metus ornare faucibus. Fusce aliquet faucibus ultricies. Morbi semper, est id tincidunt gravida, sem arcu adipiscing lacus, ac bibendum nulla leo eu purus. Quisque nec diam sed risus consectetur a ccumsan quis quis nibh. Vestibulum id purus lorem. Donec eu magna a metus ornare faucibus. Fusce aliquet faucibus ultricies. Morbi semper, est id tincidunt gravida, sem arcu adipiscing lacus, ac bibendum nulla leo eu purus. Quisque nec diam sed risus consectetur a ccumsan quis quis nibh. Vestibulum id purus lorem.</p>
  </main>

  <div class="signature">
    <div class="signature-name">Elias Marrow</div>
    <div class="signature-role">Co-Founder &amp; CEO</div>
  </div>

  <div class="memberships">
    <span class="badge-panel" role="img" aria-label="Brackwell Panel membership badge"></span>
    <span class="badge-tove" role="img" aria-label="TOVE membership badge"></span>
  </div>

  <footer class="contact-strip">
    <span class="contact-item">
      <svg viewBox="0 0 10 10" aria-hidden="true"><path d="M2 0.5 L3.8 2.6 L2.9 3.7 C3.5 5 4.8 6.3 6.2 7 L7.3 6.1 L9.5 7.9 L8.3 9.5 C4.5 9.2 0.8 5.5 0.5 1.7 Z"/></svg>
      (555) 014-2222
    </span>
    <span class="contact-item">
      <svg viewBox="0 0 10 10" aria-hidden="true"><path d="M2.5 0.5 H7.5 V3 H9.5 V7.5 H7.5 V9.5 H2.5 V7.5 H0.5 V3 H2.5 Z M3.5 1.5 V3 H6.5 V1.5 Z M3.5 6 V8.5 H6.5 V6 Z"/></svg>
      (555) 014-7701
    </span>
    <span class="contact-item">
      <svg viewBox="0 0 10 10" aria-hidden="true"><path d="M5 0.3 C7.2 0.3 8.6 2 8.6 3.8 C8.6 6.2 5 9.7 5 9.7 C5 9.7 1.4 6.2 1.4 3.8 C1.4 2 2.8 0.3 5 0.3 Z M5 2.5 A1.3 1.3 0 1 0 5 5.1 A1.3 1.3 0 1 0 5 2.5 Z"/></svg>
      2480 Alder Ridge Road, Fenwick, MI 48600
    </span>
  </footer>
</section>

<section class="sheet letter-back" aria-label="Letterhead back cover">
  <span class="binder-tab" aria-hidden="true"></span>
  <span class="cover-mark" aria-hidden="true"></span>
  <div class="cover-name">VARENNE</div>
  <div class="cover-tagline">ESTATE AGENTS</div>
</section>

</body>
</html>
```